Creation of a label for a sub brand of the Golden Comb Store and a logo for the label

We need a label to go on honey jars for a sub brand of the Golden Comb Store called Nectar Field Guy. This brand is up market and aimed at discerning consumers, foodies and raw honey connoisseurs. It may be available online as well as through delicatessens and up market supermarkets. We want the brand to built around Nectar Field Guy who goes out to seek the best quality raw monofloral honeys available. The label needs to show an image of me, with a friendly demeanour. See my response to a message that outlines more about the image.

Target Market(s)

Our target audience is upmarket consumers who appreciate high-quality products and are interested in the traceability of the product, organic production methods, and high bioactivity of the honey. They love raw honey and appreciate the different flavours available from a range of different plants and trees. They despise mass produced supermarket honey.

Industry/Entity Type

Artisan food

Requirements
Must have
• The image for Nectar Field Guy should probably be a photo, not a graphic likeness. You could use a substitute image for the moment but posed in a way that I could replicate.
Nice to have
• See the brief

```html
<!DOCTYPE html>
<html lang="en">
<head>
<meta charset="utf-8">
<title>Nectar Field Guy – Wild Lavender Honey Label</title>
<link href="https://fonts.googleapis.com/css2?family=Playfair+Display:wght@700&family=Montserrat:wght@400;500;600&family=Parisienne&family=Archivo:wght@400;700;900&display=swap" rel="stylesheet">
<style>
  :root {
    --bg: #eeeeef;
    --label-cream: #efe2bd;
    --label-cream-light: #f4ead0;
    --lavender: #6a4f98;
    --lavender-light: #9b86c4;
    --brown: #4a3520;
    --honey: #e9a52a;
    --honey-dark: #b8701a;
    --text-dark: #2f2a25;
    --white: #ffffff;
  }
  * { box-sizing: border-box; margin: 0; padding: 0; }
  html, body { width: 885px; height: 1200px; overflow: hidden; }
  body { background: var(--bg); font-family: "Montserrat", sans-serif; color: var(--text-dark); position: relative; }

  .label {
    position: absolute;
    left: 62px;
    width: 761px;
    height: 520px;
    background: var(--label-cream);
    box-shadow: 0 2px 10px rgba(0,0,0,0.08);
  }
  .label--front { top: 40px; }
  .label--back { top: 620px; }

  /* Front */
  .brand {
    position: absolute; top: 28px; left: 0; right: 0;
    display: flex; flex-direction: column; align-items: center;
  }
  .brand__dot {
    width: 58px; height: 58px; border-radius: 50%;
    background: var(--label-cream-light); border: 2px solid var(--brown);
  }
  .brand__url {
    margin-top: 8px; font-size: 8px; letter-spacing: 1px; color: var(--brown); text-transform: uppercase;
  }
  .brand__name {
    margin-top: 6px; font-family: "Playfair Display", serif; font-weight: 700;
    font-size: 26px; letter-spacing: 1px; color: var(--brown); text-transform: uppercase;
  }
  .hero-photo {
    position: absolute; top: 178px; left: 250px; width: 260px; height: 200px;
    border-radius: 4px;
    background: radial-gradient(circle at 22% 30%, var(--lavender-light) 0%, rgba(155,134,196,0) 30%),
                linear-gradient(135deg, #f2c24f 0%, var(--honey) 50%, var(--honey-dark) 100%);
  }
  .badge {
    position: absolute; top: 166px; left: 330px; width: 100px; height: 40px;
    background: var(--honey); border: 3px solid var(--white); border-radius: 6px;
    box-shadow: 0 1px 4px rgba(0,0,0,0.15);
  }
  .badge::after {
    content: ""; position: absolute; left: 8px; right: 8px; top: 50%; height: 2px;
    margin-top: -1px; background: var(--white); opacity: 0.7;
  }
  .origin {
    position: absolute; top: 398px; left: 0; right: 0; text-align: center;
    font-size: 11px; letter-spacing: 0.5px; color: var(--text-dark); text-transform: uppercase;
  }
  .band {
    position: absolute; left: 0; right: 0; top: 432px; height: 42px; background: var(--lavender);
  }
  .band__variety {
    position: absolute; left: 265px; top: 2px;
    font-family: "Parisienne", cursive; font-size: 28px; color: var(--white); letter-spacing: 1px;
  }
  .band__weight {
    position: absolute; right: 220px; top: 12px;
    font-size: 15px; font-weight: 500; color: var(--white); letter-spacing: 1px;
  }

  /* Back */
  .nutrition {
    position: absolute; top: 36px; left: 270px; width: 220px;
    background: var(--white); border: 1px solid var(--text-dark);
    padding: 5px 7px; font-family: "Archivo", sans-serif; font-size: 9px; color: #000;
  }
  .nutrition__title { font-weight: 900; font-size: 19px; line-height: 1; border-bottom: 1px solid #000; padding-bottom: 3px; }
  .nutrition__row { display: flex; justify-content: space-between; border-bottom: 1px solid #000; padding: 2px 0; }
  .nutrition__row--thick { border-bottom-width: 5px; }
  .nutrition__row--medium { border-bottom-width: 3px; }
  .nutrition__calories { font-weight: 900; font-size: 15px; }
  .nutrition__indent { padding-left: 10px; }
  .nutrition__note { font-size: 7px; padding-top: 3px; }
  .bold { font-weight: 700; }

  .back-copy {
    position: absolute; top: 290px; left: 270px; width: 240px;
    font-size: 7.5px; line-height: 1.5; color: var(--text-dark);
  }
  .back-copy p + p { margin-top: 4px; }
</style>
</head>
<body>

<section class="label label--front">
  <div class="brand">
    <div class="brand__dot"></div>
    <div class="brand__url">www.nectarfieldguy.com</div>
    <div class="brand__name">Nectar Field Guy</div>
  </div>
  <div class="hero-photo" role="img" aria-label="Honeycomb with a honey dipper and sprigs of lavender"></div>
  <div class="badge" role="img" aria-label="Organic certification badge"></div>
  <div class="origin">Country of Origin Spain</div>
  <div class="band">
    <span class="band__variety">wild lavender</span>
    <span class="band__weight">970 G</span>
  </div>
</section>

<section class="label label--back">
  <div class="nutrition">
    <div class="nutrition__title">Nutrition Facts</div>
    <div class="nutrition__row"><span>Servings Per Container 46</span></div>
    <div class="nutrition__row nutrition__row--thick"><span class="bold">Serving Size</span><span class="bold">1 tbsp (21g)</span></div>
    <div class="nutrition__row"><span class="bold">Amount Per Serving</span></div>
    <div class="nutrition__row nutrition__row--medium"><span class="nutrition__calories">Calories</span><span class="nutrition__calories">64</span></div>
    <div class="nutrition__row"><span></span><span class="bold">% Daily Value</span></div>
    <div class="nutrition__row"><span><span class="bold">Total Fat</span> 0g</span><span class="bold">0%</span></div>
    <div class="nutrition__row"><span><span class="bold">Sodium</span> 1mg</span><span class="bold">0%</span></div>
    <div class="nutrition__row"><span><span class="bold">Total Carbohydrate</span> 17g</span><span class="bold">6%</span></div>
    <div class="nutrition__row nutrition__indent"><span>Total Sugars 17g</span></div>
    <div class="nutrition__row nutrition__row--thick"><span><span class="bold">Protein</span> 0g</span></div>
    <div class="nutrition__note">Not a significant source of other nutrients.</div>
  </div>
  <div class="back-copy">
    <p>Raw unfiltered honey gathered from wild lavender in the hills of Spain.</p>
    <p>Store in a cool dry place. Natural crystallisation is a sign of quality.</p>
    <p>Ingredients: 100% raw lavender honey.</p>
    <p>Best before: see lid.</p>
  </div>
  <div class="band"></div>
</section>

</body>
</html>
```